Flyer für Lach- und Humorworkshops
Zielgruppe
Ich biete Lach- und Humorworkshops an für Unternehmen und Privatpersonen, für mehr Lebensfreude und Erfolg, ob privat oder im Business.
Aufgabenstellung
- DIN A6
- Textvorgabe im Word kann auch gekürzt werden, je nach Platz auf dem Flyer
- Schlagwörter wie 'Lachen' in der Schrift 'Licorice' so wie auf der Website

```html
<!DOCTYPE html>
<html lang="de">
<head>
<meta charset="utf-8">
<title>Lachwerk – Flyer Lach-Workshop</title>
<link rel="stylesheet" href="https://fonts.googleapis.com/css2?family=Nunito:wght@300;400;700;800&family=Shadows+Into+Light+Two&display=swap">
<style>
  :root{
    --page:#e9e7e2;
    --paper:#ffffff;
    --ink:#1c1c1c;
    --gold:#dcac58;
    --gold-deep:#c9953f;
    --tan:#c9a67a;
    --photo:#b9b3ad;
    --white:#ffffff;
  }
  *{box-sizing:border-box;margin:0;padding:0}
  html,body{width:1200px;height:889px;overflow:hidden;background:var(--page)}
  body{font-family:"Nunito",sans-serif}
  .flyer{
    position:absolute;left:309px;top:31px;width:582px;height:826px;
    background:var(--paper);overflow:hidden;
    box-shadow:0 2px 10px rgba(0,0,0,.12);
  }
  .flyer__shapes{position:absolute;inset:0;width:100%;height:100%}
  .brand{
    position:absolute;left:10px;top:34px;line-height:64px;
    font-family:"Nunito",sans-serif;font-weight:300;font-size:46px;
    color:var(--tan);letter-spacing:1px;
  }
  .headline{
    position:absolute;left:22px;top:341px;line-height:30px;
    font-family:"Shadows Into Light Two",cursive;font-weight:400;font-size:22px;
    color:var(--gold);letter-spacing:.5px;text-transform:uppercase;white-space:nowrap;
  }
  .copy{
    position:absolute;left:9px;top:415px;width:308px;
    color:var(--white);text-align:center;font-size:11.9px;line-height:17.4px;
    white-space:nowrap;
  }
  .copy h2{font-size:11.9px;font-weight:800}
  .copy p{font-weight:400}
  .copy section+section{margin-top:17.4px}
  .copy strong{font-weight:800}
  .topics{
    position:absolute;left:332px;top:616px;width:262px;
    list-style:none;color:var(--ink);
    font-weight:800;font-size:15.6px;line-height:21.3px;text-align:center;white-space:nowrap;
  }
  .topics li{position:relative}
  .topics li::before{
    content:"";position:absolute;left:8px;top:8px;width:5px;height:5px;
    border-radius:50%;background:var(--ink);
  }
  .registration{
    position:absolute;right:29px;top:741px;text-align:right;color:var(--ink);
  }
  .registration__label{font-size:9.5px;letter-spacing:1px;font-weight:400;line-height:12px}
  .registration__phone{font-size:15px;font-weight:800;margin-top:5px;line-height:18px}
  .website{
    position:absolute;left:393px;top:796px;width:166px;height:23px;
    border-radius:12px;background:var(--ink);color:var(--white);
    font-size:11.5px;font-weight:700;line-height:23px;padding-left:14px;
  }
</style>
</head>
<body>
<article class="flyer">
  <svg class="flyer__shapes" viewBox="0 0 458 650" preserveAspectRatio="none">
    <defs>
      <linearGradient id="goldFade" x1="1" y1="0" x2="0" y2="1">
        <stop offset="0" stop-color="#4a4036"/>
        <stop offset="1" stop-color="#d9b271"/>
      </linearGradient>
      <linearGradient id="goldBlob" x1="0" y1="1" x2="1" y2="0">
        <stop offset="0" stop-color="#f1e4cc"/>
        <stop offset="1" stop-color="#d3ad6e"/>
      </linearGradient>
      <clipPath id="paperClip"><rect width="458" height="650"/></clipPath>
    </defs>
    <g clip-path="url(#paperClip)">
      <polygon points="0,110 458,541 458,650 0,650" fill="var(--ink)"/>
      <line x1="258" y1="10" x2="205" y2="68" stroke="url(#goldFade)" stroke-width="36" stroke-linecap="round"/>
      <line x1="2" y1="156" x2="62" y2="216" stroke="var(--gold)" stroke-width="24" stroke-linecap="round"/>
      <circle cx="440" cy="290" r="58" fill="url(#goldBlob)"/>
      <circle cx="325" cy="165" r="158" fill="var(--photo)" role="img" aria-label="Portraitfoto der lachenden Trainerin"/>
      <circle cx="98" cy="139" r="36" fill="var(--photo)" role="img" aria-label="Foto: Trainerin lacht herzlich"/>
      <circle cx="405" cy="548" r="160" fill="var(--gold)"/>
      <circle cx="377" cy="418" r="38" fill="var(--gold-deep)" opacity=".35"/>
      <circle cx="367" cy="368" r="36" fill="var(--photo)" role="img" aria-label="Foto: Trainerin mit Lachen-Shirt"/>
    </g>
  </svg>

  <div class="brand">Lachwerk</div>
  <h1 class="headline">Lass uns lachen</h1>

  <div class="copy">
    <section>
      <h2>Warum lachen?</h2>
      <p><strong>Lachen</strong> ist einfach, gesund und macht glücklich.<br>Lachen ist eine universelle Sprache, die verbindet.<br>Lachen ist sofort wirksam und nachhaltig zugleich.<br>Lachen ist ganzheitlich, nachhaltig und sinnvoll.</p>
    </section>
    <section>
      <h2>Lach-Workshop</h2>
      <p>Du suchst eine besondere Teambuilding Aktivität?<br>Wie wäre es mit einer kurzen Auszeit aus dem<br>Alltag, die lustig, gesund, nachhaltig und sinnvoll<br>ist?<br>In einem Lach-Workshop geht es in erster Linie<br>darum, gemeinsam Spass zu haben und ausgiebig<br>zu lachen. Euch erwartet ein abwechslungsreicher<br>Mix aus einfachen, spielerischen und kreativen<br>Übungen.</p>
    </section>
    <section>
      <h2>Humor im Business – für ein positives<br>Betriebsklima</h2>
      <p><strong>Lachen</strong> ist gesund – das gilt nicht nur für unsere<br>persönliche Gesundheit, sondern auch für ein<br>Unternehmen.</p>
    </section>
  </div>

  <ul class="topics">
    <li>Teambuilding</li>
    <li>Persönlichkeitsentwicklung</li>
    <li>Stressmanagement</li>
    <li>Gesundheit &amp; Wohlbefinden</li>
    <li>Kreaktivität &amp; Innovation</li>
  </ul>

  <div class="registration">
    <div class="registration__label">REGISTRATION:</div>
    <div class="registration__phone">+49 1520 000000</div>
  </div>

  <div class="website">lachwerk-beispiel.de</div>
</article>
</body>
</html>
```